Enterprise image desing

The designs are for a fashion store for young men and women.
Updates

Los diseƱos parecen similares

Target Market(s)

Young

Font styles to use
Sans Serif

Colors
ec1f27
ffffff
1b1b1b

Requirements
Must have
• Use clean and modern sources
Nice to have
• n / a
Should not have
• n / a

```html
<!DOCTYPE html>
<html lang="en">
<head>
<meta charset="utf-8">
<title>Velora Stationery</title>
<link href="https://fonts.googleapis.com/css2?family=Work+Sans:wght@400;500;700&display=swap" rel="stylesheet">
<style>
:root{
  --navy:#0a2a4a;
  --red:#e3202b;
  --white:#ffffff;
  --ink:#1b1b1b;
  --muted:#8a8f96;
  --stage:#d7d6d4;
  --flap:#e6e7e9;
}
*{box-sizing:border-box;margin:0;padding:0}
html,body{width:1037px;height:1200px;overflow:hidden}
body{background:var(--stage);font-family:"Work Sans",sans-serif;color:var(--ink);position:relative}
.piece{position:absolute;box-shadow:0 2px 6px rgba(0,0,0,.18)}
.brand{display:flex;align-items:center;gap:6px;font-weight:700;color:var(--navy);letter-spacing:.02em;line-height:1}
.brand .mark{display:block;background:var(--red)}
.brand.on-dark{color:var(--white)}
.contact{list-style:none;font-size:5.6px;color:var(--ink);line-height:1.35}
.contact li{display:flex;align-items:center;gap:4px}
.contact li::before{content:"";width:3px;height:3px;border-radius:50%;background:var(--red)}
.contact .accent{color:var(--red)}
.address{font-size:5.6px;text-align:right;line-height:1.35;color:var(--ink)}
.footer-band{position:absolute;left:0;bottom:0;width:100%;display:block}

/* letterhead */
.sheet-back{left:141px;top:104px;width:358px;height:486px;background:var(--navy)}
.letterhead{left:86px;top:59px;width:358px;height:486px;background:var(--white)}
.letterhead .brand{position:absolute;left:29px;top:31px;font-size:24px;gap:8px}
.letterhead .brand .mark{width:24px;height:22px}
.letter-body{position:absolute;left:29px;top:132px;width:300px;color:var(--muted)}
.letter-body .greeting{font-size:9.5px;margin-bottom:20px}
.letter-body p{font-size:6.2px;line-height:1.45;margin-bottom:8px}
.signature{position:absolute;left:29px;top:370px;width:110px;height:18px;background:linear-gradient(90deg,#e4e5e7,#f2f2f3)}
.letterhead .rule{position:absolute;left:26px;right:30px;top:434px;height:1px;background:var(--red)}
.letterhead .contact{position:absolute;left:26px;top:441px}
.letterhead .address{position:absolute;right:30px;top:441px}

/* business cards */
.card-front{left:569px;top:81px;width:198px;height:113px;background:var(--white)}
.card-front .brand{position:absolute;right:12px;top:12px;font-size:11.5px;gap:4px}
.card-front .brand .mark{width:11px;height:10px}
.card-front .person{position:absolute;left:12px;top:48px}
.person .name{font-size:6.2px;font-weight:700;color:var(--red);letter-spacing:.02em}
.person .role{font-size:5px;color:var(--ink)}
.card-front .rule{position:absolute;left:12px;right:12px;top:67px;height:1px;background:var(--navy)}
.card-front .contact{position:absolute;left:12px;top:75px;font-size:5px}
.card-front .address{position:absolute;right:12px;top:75px;font-size:5px}
.card-back{left:779px;top:81px;width:198px;height:113px;background:var(--navy)}
.card-back .brand{position:absolute;left:36px;top:47px;font-size:17px;gap:6px}
.card-back .brand .mark{width:17px;height:16px}
.card-back .web{position:absolute;left:0;right:0;top:98px;text-align:center;font-size:4.6px;color:var(--white)}
.card-back .web span{color:var(--red)}

/* long envelope */
.envelope-long{left:529px;top:226px;width:353px;height:166px;background:var(--white)}
.envelope-long .brand{position:absolute;left:17px;top:19px;font-size:19px;gap:6px}
.envelope-long .brand .mark{width:19px;height:17px}
.envelope-long .rule{position:absolute;left:17px;right:17px;top:115px;height:1px;background:var(--red)}
.envelope-long .contact{position:absolute;left:17px;top:122px}
.envelope-long .address{position:absolute;right:17px;top:122px}

/* pocket envelope */
.envelope-pocket{left:626px;top:346px;width:352px;height:248px;background:var(--navy);overflow:hidden}
.envelope-pocket .flap{position:absolute;left:0;top:0;width:100%;height:120px;display:block}
.envelope-pocket .brand{position:absolute;left:109px;top:172px;font-size:19px;gap:6px}
.envelope-pocket .brand .mark{width:19px;height:17px}

/* folder */
.folder-back{left:212px;top:690px;width:311px;height:446px;background:var(--navy)}
.folder-back .brand{position:absolute;left:39px;top:382px;font-size:22px;gap:7px}
.folder-back .brand .mark{width:22px;height:20px}
.folder-front{left:523px;top:690px;width:311px;height:446px;background:#f4f4f5}
.folder-front .brand{position:absolute;left:69px;top:38px;font-size:25px;gap:8px}
.folder-front .brand .mark{width:25px;height:23px}
.folder-front .base{position:absolute;left:0;bottom:20px;width:100%;height:56px;background:var(--navy)}
.folder-front .contact{position:absolute;left:20px;top:18px;color:var(--white)}
.folder-front .address{position:absolute;right:19px;top:16px;color:var(--white)}
</style>
</head>
<body>

<section class="piece sheet-back" aria-hidden="true"></section>

<article class="piece letterhead">
  <div class="brand"><span class="mark"></span>VELORA</div>
  <div class="letter-body">
    <p class="greeting">Dear sir,</p>
    <p>Thank you for your interest in our new collection for the coming season. We design clothing for young people who value comfort, clean lines and honest materials. Our team is glad to share the details of the catalogue and the current wholesale terms with you.</p>
    <p>Each piece is cut and sewn in small runs, checked by hand and packed with care before it leaves our workshop. We update the range every few weeks, so the shelves in your store always feel fresh. Orders placed before the end of the month ship within ten days, and we cover the cost of delivery for any order above the agreed minimum amount.</p>
    <p>We would be pleased to visit your store and present the samples in person. Please let us know which days suit you best next week. Our sales team can also arrange a short video call if a meeting on site is not possible.</p>
    <p>Thank you again for your time. We look forward to working together and to seeing our garments in your windows soon.</p>
  </div>
  <div class="signature" role="img" aria-label="Handwritten signature"></div>
  <div class="rule"></div>
  <ul class="contact">
    <li>+593 7 000-1234</li>
    <li>mruiz@velora.com</li>
    <li>www.<span class="accent">velora</span>.com</li>
  </ul>
  <p class="address">Calle Central y<br>Robles,<br>Ecuador, EC000000</p>
  <svg class="footer-band" viewBox="0 0 358 16" width="358" height="16" preserveAspectRatio="none" aria-hidden="true">
    <path d="M0 16 V12 H190 C208 12 212 4 232 4 H358 V16 Z" fill="var(--navy)"/>
    <path d="M0 8 H186 C204 8 208 1 228 1 H358" fill="none" stroke="var(--red)" stroke-width="1.6"/>
  </svg>
</article>

<article class="piece card-front">
  <div class="brand"><span class="mark"></span>VELORA</div>
  <div class="person">
    <p class="name">MARCO RUIZ PAREDES</p>
    <p class="role">Gerente General</p>
  </div>
  <div class="rule"></div>
  <ul class="contact">
    <li>+593 7 000-1234</li>
    <li>+593 98 000-5678</li>
    <li>mruiz@velora.com</li>
    <li>www.<span class="accent">velora</span>.com</li>
  </ul>
  <p class="address">Calle Central y<br>Robles,<br>Ecuador, EC000000</p>
  <svg class="footer-band" viewBox="0 0 198 9" width="198" height="9" preserveAspectRatio="none" aria-hidden="true">
    <path d="M0 9 V7 H104 C114 7 116 2 126 2 H198 V9 Z" fill="var(--navy)"/>
    <path d="M0 4.5 H102 C111 4.5 113 0.6 123 0.6 H198" fill="none" stroke="var(--red)" stroke-width="1.2"/>
  </svg>
</article>

<article class="piece card-back">
  <div class="brand on-dark"><span class="mark"></span>VELORA</div>
  <p class="web">www.<span>velora</span>.com</p>
</article>

<article class="piece envelope-long">
  <div class="brand"><span class="mark"></span>VELORA</div>
  <div class="rule"></div>
  <ul class="contact">
    <li>+593 7 000-1234</li>
    <li>mruiz@velora.com</li>
    <li>www.<span class="accent">velora</span>.com</li>
  </ul>
  <p class="address">Calle Central y<br>Robles,<br>Ecuador, EC000000</p>
  <svg class="footer-band" viewBox="0 0 353 14" width="353" height="14" preserveAspectRatio="none" aria-hidden="true">
    <path d="M0 14 V10 H185 C203 10 207 3 225 3 H353 V14 Z" fill="var(--navy)"/>
    <path d="M0 6.5 H182 C199 6.5 203 0.8 221 0.8 H353" fill="none" stroke="var(--red)" stroke-width="1.6"/>
  </svg>
</article>

<article class="piece envelope-pocket">
  <svg class="flap" viewBox="0 0 352 120" width="352" height="120" preserveAspectRatio="none" aria-hidden="true">
    <path d="M0 0 H352 V100 L330 120 L315 110 H37 L22 120 L0 100 Z" fill="var(--flap)"/>
    <path d="M37 110 H315" stroke="#cfd1d4" stroke-width="1"/>
  </svg>
  <div class="brand on-dark"><span class="mark"></span>VELORA</div>
</article>

<article class="piece folder-back">
  <div class="brand on-dark"><span class="mark"></span>VELORA</div>
</article>

<article class="piece folder-front">
  <div class="brand"><span class="mark"></span>VELORA</div>
  <div class="base">
    <ul class="contact">
      <li>+593 7 000-1234</li>
      <li>mruiz@velora.com</li>
      <li>www.<span class="accent">velora</span>.com</li>
    </ul>
    <p class="address">Calle Central y<br>Robles,<br>Ecuador, EC000000</p>
  </div>
</article>

</body>
</html>
```